Letter Head Design - Finance industry

Design a letterhead to match the logo. Needs to be clean, simple and crisp. I'm open to suggestions. Will be using the logo that was submitted last with the W crossed over

Target Market(s)

Small medium businesses and government department's

Industry/Entity Type

Industry

Font styles to use
Sans Serif

Colors
cadf82
bcd85c
acd036
9bcb3c
e9e9e9
aaaaaa
000000
7f7f7f
b7b7b7

Requirements
Must have
• Need to display: Logo, Business address, ABN number, ASIC register number, contact phone, website, company email. Details are as per below:

Suite 4B Level 17
Marlowe Crest House
9 Tindall Lane
Sydney NSW 2000
Landline Ph: 02 5193 4620
Ph: 1300 4719 55
Email: enquiries@coinharbourco.com.au
W: www.coinharbourco.com.au

On the footer, the details below need to be specified:
ABN: 47 381 950 623
ASIC Registration Number: 31 749218605

Should not have
• No imagery or design that is not in line with the logo

```html
<!DOCTYPE html>
<html lang="en">
<head>
<meta charset="utf-8">
<title>Coin Harbour Co Letterhead</title>
<link rel="stylesheet" href="https://fonts.googleapis.com/css2?family=EB+Garamond:wght@400;500&display=swap">
<style>
  :root {
    --backdrop: #e9e9e9;
    --paper: #ffffff;
    --ink: #000000;
    --ink-soft: #7f7f7f;
    --ink-muted: #aaaaaa;
    --brand-green: #9bcb3c;
    --rule-green: #bcd85c;
    --tint-green: #cadf82;
  }
  * { box-sizing: border-box; margin: 0; padding: 0; }
  html, body {
    width: 1200px;
    height: 900px;
    overflow: hidden;
    background: var(--backdrop);
  }
  .canvas {
    position: relative;
    width: 1200px;
    height: 900px;
  }
  .letterhead {
    position: absolute;
    left: 306px;
    top: 35px;
    width: 589px;
    height: 832px;
    background: var(--paper);
    overflow: hidden;
    font-family: "EB Garamond", Garamond, serif;
    color: var(--ink);
    box-shadow: 0 2px 10px rgba(0,0,0,0.18);
  }
  .backdrop-mark {
    position: absolute;
    left: 0;
    top: 0;
    width: 589px;
    height: 832px;
  }
  .brand {
    position: absolute;
    left: 54px;
    top: 62px;
    display: flex;
    align-items: center;
    gap: 10px;
  }
  .brand-dot {
    width: 30px;
    height: 30px;
    border-radius: 50%;
    background: var(--brand-green);
  }
  .brand-name {
    font-size: 26px;
    font-weight: 400;
    color: #4d4d4d;
    letter-spacing: 0.2px;
    white-space: nowrap;
  }
  .address {
    position: absolute;
    left: 293px;
    top: 51px;
    font-size: 8px;
    line-height: 10.3px;
    font-weight: 500;
    color: var(--ink);
  }
  .contact {
    position: absolute;
    left: 397px;
    top: 51px;
    font-size: 8px;
    line-height: 10.3px;
    color: var(--ink-soft);
  }
  .letter-body {
    position: absolute;
    left: 78px;
    top: 219px;
    width: 372px;
    font-size: 11px;
    line-height: 15.6px;
  }
  .letter-body p + p { margin-top: 15.6px; }
  .footer-rule {
    position: absolute;
    left: 78px;
    top: 766px;
    width: 474px;
    height: 1px;
    background: var(--rule-green);
  }
  .registration {
    position: absolute;
    left: 78px;
    top: 778px;
    font-size: 8px;
    line-height: 11px;
    font-weight: 500;
  }
</style>
</head>
<body>
<div class="canvas">
  <article class="letterhead">
    <svg class="backdrop-mark" viewBox="0 0 589 832" aria-hidden="true">
      <circle cx="500" cy="445" r="200" fill="var(--tint-green)" opacity="0.55"/>
    </svg>

    <header>
      <div class="brand">
        <span class="brand-dot"></span>
        <span class="brand-name">Coin Harbour Co</span>
      </div>
      <address class="address">
        Suite 4B Level 17<br>
        Marlowe Crest House<br>
        9 Tindall Lane<br>
        Sydney NSW 2000
      </address>
      <address class="contact">
        Landline: 02 5193 4620<br>
        Phone: 1300 4719 55<br>
        Email: enquiries@coinharbourco.com.au<br>
        www.coinharbourco.com.au
      </address>
    </header>

    <section class="letter-body">
      <p>Lorem ipsum dolor sit amet, eum in accusam scripserit, ius oblique repudiandae cu. Ea tation indoctum sed, his id inciderint intellegebat, eam et illum suavitate. Vix te discere accumsan disputando, te elit regione cum, id vis veniam prompta docendi. Cibo doming mediocrem an usu, stet solet corpora mel ex. An homero petentium quo.</p>
      <p>Error doming ius ne, pri ut labores scaevola. Est noster offendit cu, ne platonem comprehensam sea, at vel iudico essent. Ea eum equidem docendi sententiae, magna audiam ne quo. Natum rationibus mea ei, eum in clita soleat. Meis omnesque an qui, mea id oblique civibus copiosae, sit et quot aliquam forensibus. Hinc ignota dolorum an eos, hinc recusabo an nam.</p>
      <p>Inimicus scriptorem scribentur cum eu, vel ne vivendo ancillae intellegam, in reque equidem neglegentur mei. Dico nullam patrioque ad per, est ea tritani placerat, at duo atqui deserunt. Eos facer viderer te. Ius illum ceteros volutpat cu, error dolorum eu pro, has te dicit definitionem.</p>
      <p>Dico omittantur mediocritatem ea sed, te atqui congue tantas duo. Debet mucius ei qui, eam in offendit senserit instructior, altera civibus eum te. Ei sit facer laudem discere, prodesset liberavisse in pro, usu sale fierent ne. Labore inermis ullamcorper sea at, putant dissentias necessitatibus mea cu. At mel soluta dolores repudiare, adhuc convenire cu pri.</p>
      <p>Essent sanctus at ius, sea in dicant integre, dolorem tibique ullamcorper ne has. Te verterem euripidis nam. Vis ullum perpetua no, at mel deserunt electram honestatis. Minimum oportere principes mel ne.</p>
    </section>

    <footer>
      <div class="footer-rule"></div>
      <p class="registration">
        ABN: 47 381 950 623<br>
        ASIC Registration Number: 31 749218605
      </p>
    </footer>
  </article>
</div>
</body>
</html>
```